Crime/mystery/thriller novel cover design

I am looking to get a cover designed for a novel. It is a crime/mystery/thriller set in Liverpool, England, between the 1970s and current day. I have permission to use some paintings by an artist for the cover, so it just needs put together and jazzed up. I am looking for something which has a fairly classic feel (so not just pulp airport thriller trash) but with some flair nonetheless.
The novel will be paperback, 127mm x 203mm with approx 18mm spine width. Can be gloss or matt cover, would be interesting to discuss.
The title is:
THE HARBOUR LANTERN
Author name:
GORDON T. VESELKA
Publisher:
BRIVOLTA PUBLISHING LTD (or simply BRIVOLTA)

I am still working on the back cover blurb but I will upload this when finished.
There are 4 images I could use for the cover though my favourite is the one called Dusk, Quayside Terraces.

```html
<!DOCTYPE html>
<html lang="en">
<head>
<meta charset="utf-8">
<title>The Harbour Lantern — Front Cover</title>
<link href="https://fonts.googleapis.com/css2?family=Cinzel:wght@500&family=Parisienne&family=Oswald:wght@500&family=Montserrat:wght@500&display=swap" rel="stylesheet">
<style>
  :root {
    --backdrop: #c4c5c7;
    --ink-dark: #1e1f1d;
    --charcoal: #2b2d2a;
    --olive: #4a5a35;
    --moss: #6b7a3a;
    --ember: #e0641c;
    --flame: #f3a21f;
    --glow: #f7d64a;
    --title-gold: #f1ea8a;
    --label-white: #f4f4f4;
  }
  * { box-sizing: border-box; margin: 0; padding: 0; }
  html, body {
    width: 1200px; height: 900px; overflow: hidden;
    background: var(--backdrop);
  }
  .stage {
    width: 1200px; height: 900px;
    display: flex; align-items: center; justify-content: center;
  }
  .cover {
    position: relative;
    width: 500px; height: 800px;
    overflow: hidden;
    background: var(--charcoal);
    box-shadow: 0 10px 30px rgba(0,0,0,0.25);
  }
  .cover-art {
    position: absolute; inset: 0;
    background:
      radial-gradient(ellipse 60% 18% at 45% 66%, rgba(247,214,74,0.85), rgba(247,214,74,0) 70%),
      linear-gradient(180deg,
        var(--ink-dark) 0%,
        var(--charcoal) 14%,
        var(--olive) 30%,
        var(--moss) 40%,
        var(--flame) 52%,
        var(--ember) 62%,
        var(--flame) 70%,
        var(--ember) 80%,
        #3a2414 100%);
  }
  .title {
    position: absolute; left: 40px; top: 70px; right: 30px;
    color: var(--title-gold);
    font-weight: normal;
    text-shadow: 0 2px 4px rgba(0,0,0,0.45);
  }
  .title-small {
    display: block;
    font-family: "Cinzel", serif;
    font-size: 26px; letter-spacing: 1px; line-height: 1;
  }
  .title-main {
    display: block;
    font-family: "Cinzel", serif;
    font-size: 46px; letter-spacing: 1px; line-height: 1.05;
  }
  .title-script {
    display: block;
    font-family: "Parisienne", cursive;
    font-size: 100px; line-height: 1;
    white-space: nowrap;
    margin: 0 0 0 50px;
  }
  .author {
    position: absolute; right: 40px; top: 470px;
    font-family: "Oswald", sans-serif;
    font-weight: 500;
    font-size: 34px; letter-spacing: 1px;
    color: var(--title-gold);
    border-bottom: 2px solid var(--title-gold);
    padding-bottom: 4px;
    text-shadow: 0 2px 4px rgba(0,0,0,0.4);
  }
  .publisher {
    position: absolute; right: 0; bottom: 0;
    background: var(--ink-dark);
    color: var(--label-white);
    font-family: "Montserrat", sans-serif;
    font-weight: 500;
    font-size: 17px; letter-spacing: 1.5px;
    padding: 12px 18px;
  }
</style>
</head>
<body>
  <main class="stage">
    <section class="cover">
      <div class="cover-art" role="img" aria-label="Painting: Dusk, Quayside Terraces — a ship silhouetted on the water against a blazing orange and yellow sky under dark green clouds"></div>
      <h1 class="title">
        <span class="title-small">THE</span>
        <span class="title-main">HARBOUR</span>
        <span class="title-script">Lantern</span>
      </h1>
      <p class="author">GORDON T. VESELKA</p>
      <p class="publisher">BRIVOLTA</p>
    </section>
  </main>
</body>
</html>
```